Book Cover Design for Carry the HOPE

The title continues with shaped by Heaven's Outline to Pursue Excellence in kindness to neighbours. So HOPE is an acronym for Heaven's Outline Pursuing Excellence. I wrote the book based on what God taught me when my adult daughter passed away. I failed to recognize her gifts of helping people feel valued and loved. Through this discovery, I recognized I had an identity crisis which prevented me from using the gifts God gave me to serve others. The book chapters include: (1) Carry the HOPE, (2) The Author of the HOPE, (3) Beware the HOPE Robber, (4) Defenders of the HOPE, (5) The Purpose of the HOPE, (6) The Manifestation of the HOPE, (7) The Empowerment of the HOPE and (9) The Reward of the HOPE. Please let me know what other information would be helpful in designing my book cover
Target Market(s)
The book is intended for Christians who surrendered just enough to get saved but did not surrender enough for God to transform them to become more Christ-like.
Industry/Entity Type
Christian
Requirements
Must have
- Please ensure each letter in the word HOPE is a different color. Next, ensure the first leet of the words Heaven's Outline and Pursuing Excellence in the make in .... are the same color as the associate letter in HOPE.
For this project, I just want the front cover. I will create a separate paid project for the selected designer to complete the spine and back cover before publishing through Brindlecart.
Nice to have
- Is it possible to make the cover look like a gift you would receive
I also attached potential design ideas for layout. I want to see your creativity come out in the design.
Should not have
- Not applicable

```html
<!DOCTYPE html>
<html lang="en">
<head>
<meta charset="utf-8">
<title>Carry the HOPE — Book Cover Wrap</title>
<link rel="stylesheet" href="https://fonts.googleapis.com/css2?family=Pinyon+Script&family=Lilita+One&family=Kaushan+Script&family=Dancing+Script:wght@600&family=Oswald:wght@500;700&family=Lato:ital,wght@0,400;1,400&display=swap">
<style>
  :root {
    --back-black: #050505;
    --back-grey: #2a2a2a;
    --teal-text: #19b5c8;
    --red-accent: #d11f1f;
    --white: #ffffff;
    --muted-grey: #8a8a8a;
    --spine-yellow: #ffcc33;
    --spine-orange: #f39a1b;
    --front-top: #fbe9ea;
    --front-mid: #f8c27a;
    --front-low: #f08a1a;
    --title-orange: #f7941d;
    --hope-h: #7b2d8e;
    --hope-o: #f28c1b;
    --hope-p: #d6257a;
    --hope-e: #1a9bb0;
    --band-dark: #3b2a22;
    --band-light: #e7e7e7;
    --ink: #111111;
  }
  * { box-sizing: border-box; margin: 0; padding: 0; }
  html, body { width: 1200px; height: 894px; overflow: hidden; background: #ffffff; }
  .cover-wrap { position: relative; width: 1200px; height: 894px; display: flex; }

  /* Back cover */
  .back-cover {
    position: relative; width: 618px; height: 894px;
    background: radial-gradient(ellipse at 60% 40%, var(--back-grey) 0%, var(--back-black) 70%);
    color: var(--teal-text); overflow: hidden;
  }
  .back-ornament {
    position: absolute; border-radius: 50%;
    background: radial-gradient(circle, rgba(90,90,90,0.35) 0%, rgba(0,0,0,0) 70%);
  }
  .back-ornament.top-right { right: -40px; top: 20px; width: 260px; height: 220px; }
  .back-ornament.top-left { left: -60px; top: -40px; width: 240px; height: 200px; }
  .back-ornament.accent-left {
    left: 0; top: 620px; width: 90px; height: 130px; border-radius: 0 40px 40px 0;
    background: linear-gradient(90deg, rgba(180,20,20,0.8), rgba(120,10,10,0.2));
  }
  .author-name {
    position: absolute; top: 24px; width: 100%; text-align: center;
    font-family: "Pinyon Script", cursive; font-size: 54px; color: var(--white);
  }
  .back-tagline {
    position: absolute; top: 92px; width: 100%; text-align: center;
    font-family: "Oswald", sans-serif; font-weight: 500; font-size: 15px;
    letter-spacing: 1px; color: var(--red-accent);
  }
  .back-heading {
    position: absolute; left: 66px; font-family: "Lato", sans-serif;
    font-size: 24px; color: var(--teal-text);
  }
  .back-heading.about-author { top: 140px; }
  .back-heading.about-book { top: 386px; }
  .back-body {
    position: absolute; left: 30px; width: 560px;
    font-family: "Lato", sans-serif; font-style: italic; font-size: 13.5px;
    line-height: 21px; color: var(--teal-text); text-indent: 60px;
  }
  .back-body.author-bio { top: 178px; }
  .back-body.book-blurb { top: 424px; }
  .back-info {
    position: absolute; left: 24px; font-family: "Oswald", sans-serif;
    color: var(--muted-grey); letter-spacing: 2px;
  }
  .back-info.additional { top: 762px; font-size: 18px; }
  .back-info.address { top: 800px; font-size: 18px; }
  .back-info.website { top: 832px; font-size: 11px; }

  /* Spine */
  .spine {
    position: relative; width: 66px; height: 894px;
    background: linear-gradient(90deg, var(--spine-orange), var(--spine-yellow) 55%, var(--spine-orange));
  }
  .spine-text {
    position: absolute; left: 50%; writing-mode: vertical-rl;
    transform: translateX(-50%); white-space: nowrap;
  }
  .spine-author {
    top: 18px; font-family: "Oswald", sans-serif; font-weight: 500;
    font-size: 20px; letter-spacing: 2px; color: var(--red-accent);
  }
  .spine-title {
    top: 210px; font-family: "Lilita One", sans-serif; font-style: italic;
    font-size: 28px; letter-spacing: 2px; color: var(--red-accent);
  }
  .spine-edition {
    top: 610px; font-family: "Oswald", sans-serif; font-weight: 500;
    font-size: 18px; letter-spacing: 1px; color: var(--band-dark);
  }
  .publisher-mark {
    position: absolute; left: 50%; bottom: 24px; transform: translateX(-50%);
    width: 42px; height: 42px; border-radius: 50%; background: var(--band-dark);
  }

  /* Front cover */
  .front-cover {
    position: relative; width: 516px; height: 894px; overflow: hidden;
    background: linear-gradient(180deg, var(--front-top) 0%, #fbdbd0 25%, var(--front-mid) 55%, var(--front-low) 85%);
  }
  .title-lead {
    position: absolute; left: 18px; top: 18px;
    font-family: "Lilita One", sans-serif; font-size: 44px; line-height: 46px;
    color: var(--title-orange); text-shadow: 2px 2px 0 #b65c0a;
  }
  .title-hope {
    position: absolute; right: 14px; top: 6px;
    font-family: "Lilita One", sans-serif; font-size: 128px; line-height: 140px;
    text-shadow: 3px 3px 0 rgba(60,20,70,0.45);
  }
  .hope-h { color: var(--hope-h); }
  .hope-o { color: var(--hope-o); }
  .hope-p { color: var(--hope-p); }
  .hope-e { color: var(--hope-e); }
  .subtitle {
    position: absolute; left: 30px; right: 20px; top: 160px; text-align: center;
    font-family: "Kaushan Script", cursive; font-size: 22px; line-height: 30px;
    color: var(--title-orange);
  }
  .subtitle .initial { font-size: 26px; }
  .cover-illustration {
    position: absolute; left: 0; top: 232px; width: 516px; height: 490px;
    background: radial-gradient(ellipse at 50% 45%, rgba(255,250,235,0.95) 0%, rgba(252,210,150,0.7) 35%, rgba(243,150,40,0.55) 70%, rgba(240,138,26,0) 100%);
  }
  .cover-caption {
    position: absolute; top: 722px; width: 100%; text-align: center;
    font-family: "Lato", sans-serif; font-size: 14px; color: var(--white);
  }
  .dedication-band {
    position: absolute; top: 748px; left: 0; width: 100%; height: 38px;
    background: linear-gradient(90deg, #5a3f30, var(--band-dark), #5a3f30);
    text-align: center; font-family: "Dancing Script", cursive; font-size: 22px;
    line-height: 38px; color: #f4d9b0;
  }
  .name-band {
    position: absolute; top: 790px; left: 0; width: 100%; height: 82px;
    background: linear-gradient(180deg, #ffffff, var(--band-light));
    text-align: center; font-family: "Oswald", sans-serif; font-weight: 700;
    font-size: 46px; line-height: 82px; letter-spacing: 1px; color: var(--ink);
  }
</style>
</head>
<body>
<main class="cover-wrap">
  <section class="back-cover">
    <div class="back-ornament top-left" role="img" aria-label="Faint dark floral flourish"></div>
    <div class="back-ornament top-right" role="img" aria-label="Faint dark floral flourish"></div>
    <div class="back-ornament accent-left" role="img" aria-label="Red decorative flourish"></div>
    <h1 class="author-name">Martin Ashford</h1>
    <p class="back-tagline">- CARRY THE HOPE -</p>
    <h2 class="back-heading about-author">About The Author</h2>
    <p class="back-body author-bio">This is a demo text only for representation purpose, for final copy the proper content should be edited consulting the author. This is a demo text only for representation purpose, for final copy the proper content should be edited consulting the author. This is a demo text only for representation purpose, for final copy the proper content should be edited consulting the author.</p>
    <h2 class="back-heading about-book">About The Book</h2>
    <p class="back-body book-blurb">This is a demo text only for representation purpose, for final copy the proper content should be edited consulting the author. This is a demo text only for representation purpose, for final copy the proper content should be edited consulting the author. This is a demo text only for representation purpose, for final copy the proper content should be edited consulting the author. This is a demo text only for representation purpose, for final copy the proper content should be edited consulting the author. This is a demo text only for representation purpose, for final copy the proper content should be edited consulting the author. This is a demo text only for representation purpose, for final copy the proper content should be edited consulting the author.</p>
    <p class="back-info additional">ADDITIONAL INFO TEXT</p>
    <p class="back-info address">INFO &amp; ADDRESS</p>
    <p class="back-info website">WEBSITE ADDRESS</p>
  </section>

  <section class="spine">
    <p class="spine-text spine-author">AUTHOR NAME</p>
    <p class="spine-text spine-title">CARRY THE HOPE</p>
    <p class="spine-text spine-edition">FIRST EDITION</p>
    <span class="publisher-mark" aria-hidden="true"></span>
  </section>

  <section class="front-cover">
    <p class="title-lead">CARRY<br>THE</p>
    <h2 class="title-hope"><span class="hope-h">H</span><span class="hope-o">O</span><span class="hope-p">P</span><span class="hope-e">E</span></h2>
    <p class="subtitle">shaped by <span class="initial hope-h">H</span>eaven's <span class="initial hope-o">O</span>utline to <span class="initial hope-p">P</span>ursue <span class="initial hope-e">E</span>xcellence in kindness to neighbours</p>
    <div class="cover-illustration" role="img" aria-label="Illustration of a woman silhouette with arms raised among flowers and warm sun rays"></div>
    <p class="cover-caption">recognize the 'HOPE' of people feeling VALUED and LOVED</p>
    <p class="dedication-band">- Inspired From The Life Of My Daughter -</p>
    <p class="name-band">MARTIN ASHFORD</p>
  </section>
</main>
</body>
</html>
```